Brightwell Works Capability Statement 2019

this document will be used to draw new business in so it NEEDS to be engaging and the prospective client will need to want to flip the page and read on.
this will be an engaging, ultra modern capability statement.
Pages i need created including text as per attachments capability statement 2018 REV
Fresh new Photos will need to be taken from from photo stock or similar site please do not use photos on existing attachments
Logo attached
Updates

Target Market(s)

Commercial building, facility managers, asset managers, strata markets

Industry/Entity Type

Construction Company

Colors

Designer to choose colors to be used in the design.

Requirements
Must have
• fresh, ultra modern and engaging.
• needs very fresh and crisp images, visually appealing colour scheme that draws the reader in
• - Referencing our QLD branch - covering the eastern seaboard
• - professional outfit
• - designs need to go all the way to edge of page
Nice to have
• all details in must haves
Should not have
• outdated colour scheme, outdated old - pixelated photos , not cropped in or border

```html
<!DOCTYPE html>
<html lang="en">
<head>
<meta charset="utf-8">
<title>Brightwell Works Capability Statement 2019</title>
<link href="https://fonts.googleapis.com/css2?family=Oswald:wght@500;600;700&family=Arimo:wght@400;700&display=swap" rel="stylesheet">
<style>
  :root {
    --navy: #3a3a80;
    --navy-deep: #2d2d6b;
    --orange: #f0922e;
    --orange-deep: #e9791c;
    --paper: #f5f5f3;
    --ink: #2d2d6b;
    --white: #ffffff;
    --stage: #d9d9d9;
  }
  * { margin: 0; padding: 0; box-sizing: border-box; }
  html, body { width: 1200px; height: 840px; overflow: hidden; background: var(--stage); }
  body { font-family: "Arimo", Arial, sans-serif; }
  .spread { position: relative; width: 1200px; height: 840px; display: flex; }
  .page { position: relative; width: 600px; height: 840px; background: var(--paper); overflow: hidden; }
  .page--left { border-right: 1px solid #e2e2e2; }

  .page-header { position: absolute; top: 34px; left: 30px; right: 30px; height: 50px; }
  .year-tag { position: absolute; left: 0; top: 8px; background: var(--orange); color: var(--white);
    font-family: "Oswald", sans-serif; font-weight: 600; font-size: 14px; padding: 3px 6px; }
  .doc-title { position: absolute; left: 52px; top: 11px; font-family: "Oswald", sans-serif;
    font-weight: 600; font-size: 14px; color: var(--navy); letter-spacing: .2px; }
  .brand { position: absolute; right: 0; top: 0; text-align: right; }
  .brand-name { font-family: "Arimo", sans-serif; font-weight: 700; font-size: 28px; color: var(--navy); line-height: 1; letter-spacing: -.5px; }
  .brand-tagline { font-size: 12px; color: #444; margin-top: 4px; }

  .decor { position: absolute; inset: 0; }

  .personnel { position: absolute; left: 36px; top: 112px; width: 264px; height: 650px;
    background: linear-gradient(160deg, var(--navy-deep), var(--navy)); color: var(--white); padding: 18px 18px; }
  .personnel h1 { font-family: "Oswald", sans-serif; font-weight: 700; font-size: 28px; letter-spacing: .3px; line-height: 1; margin-bottom: 12px; }
  .role { font-family: "Oswald", sans-serif; font-weight: 600; font-size: 15px; color: var(--orange); margin-bottom: 6px; }
  .bio { font-size: 11px; line-height: 14.5px; margin-bottom: 22px; }
  .bio--justify { text-align: justify; }
  .bio strong { font-weight: 700; }

  .side-copy { position: absolute; left: 316px; top: 118px; width: 270px; color: var(--white); }
  .side-copy h2 { font-family: "Oswald", sans-serif; font-weight: 600; font-size: 16px; color: var(--navy); line-height: 1.3; margin-bottom: 8px; }
  .side-copy p { font-size: 10.5px; line-height: 14px; margin-bottom: 20px; }

  .page-number { position: absolute; bottom: 34px; font-family: "Oswald", sans-serif; font-weight: 600; font-size: 13px; color: var(--navy); }
  .web { position: absolute; bottom: 32px; right: 34px; font-family: "Oswald", sans-serif; font-weight: 600; font-size: 13px; color: var(--navy); }

  .facts { position: absolute; left: 26px; top: 96px; width: 548px; height: 334px; background: var(--orange); }
  .facts-list { position: absolute; left: 10px; top: 14px; width: 250px; color: var(--navy-deep); }
  .facts-list h3 { font-family: "Oswald", sans-serif; font-weight: 600; font-size: 16px; color: var(--white); line-height: 1.1; margin-bottom: 2px; }
  .facts-list p { font-size: 11px; line-height: 14px; margin-bottom: 14px; color: #1f1f4a; }
  .quality { position: absolute; right: 10px; top: 10px; width: 272px; height: 314px; background: var(--navy); color: var(--white); padding: 16px 14px; }
  .quality h3 { font-family: "Oswald", sans-serif; font-weight: 600; font-size: 16px; color: var(--orange); line-height: 1.25; margin-bottom: 16px; }
  .quality p { font-size: 11px; line-height: 14px; margin-bottom: 14px; }

  .photo-desk { position: absolute; left: 26px; top: 430px; width: 548px; height: 334px;
    background: linear-gradient(135deg, #3b3a38 0%, #6b5e4e 45%, #2c3f66 75%, #3a3030 100%); }
</style>
</head>
<body>
<main class="spread">

  <section class="page page--left">
    <header class="page-header">
      <span class="year-tag">2019</span>
      <span class="doc-title">CAPABILITY STATEMENT</span>
      <div class="brand">
        <div class="brand-name">Brightwell Works</div>
        <div class="brand-tagline">strata painting &amp; remedial repair</div>
      </div>
    </header>

    <svg class="decor" width="600" height="840" viewBox="0 0 600 840" aria-hidden="true">
      <defs>
        <linearGradient id="orangeFade" x1="0" y1="0" x2="1" y2="1">
          <stop offset="0" stop-color="#f6a84a"/>
          <stop offset="1" stop-color="#e9791c"/>
        </linearGradient>
      </defs>
      <polygon points="26,104 310,110 600,78 600,700 360,800 26,770" fill="url(#orangeFade)"/>
    </svg>

    <svg class="decor" width="600" height="840" viewBox="0 0 600 840" role="img" aria-label="Photo of a hand writing notes with a pen on paper at a desk">
      <defs>
        <linearGradient id="handPhoto" x1="0" y1="0" x2="1" y2="1">
          <stop offset="0" stop-color="#5d6b80"/>
          <stop offset=".5" stop-color="#a68b78"/>
          <stop offset="1" stop-color="#2f3440"/>
        </linearGradient>
      </defs>
      <polygon points="318,462 600,368 600,688 326,766" fill="url(#handPhoto)"/>
    </svg>

    <article class="personnel">
      <h1>KEY PERSONNEL</h1>
      <h2 class="role">MANAGING DIRECTOR/OWNER</h2>
      <p class="bio"><strong>Daniel Ashcroft</strong> has been able to seamlessly build a team of professionals around him, all of whom are committed to the impeccable detail that is put into each and every job. It is this commitment to detail that has meant Brightwell Works has been able to successfully meet and exceed each client's individual needs, day in day out.</p>
      <h2 class="role">GENERAL MANAGER</h2>
      <p class="bio bio--justify">Brightwell Works QLD Liam Ashcroft has vast experience in the construction and trades industries from Site supervisor and project manager to operations manager and Owner operator. Liam is committed to providing the highest quality customer service to his clients</p>
      <h2 class="role">LEAD ESTIMATOR</h2>
      <p class="bio">Marco Vitale, a licensed painter and builder, heads our experienced estimating team. Marco is committed to deliver the best possible quality in customer service and price.</p>
      <h2 class="role">SENIOR PROJECT MANAGER</h2>
      <p class="bio bio--justify">Our project management division is led by Peter Konstantis. He manages a team of project managers and the daily running of the core businesses of painting and remedial projects.</p>
    </article>

    <aside class="side-copy">
      <h2>Business Development Manager:</h2>
      <p>Sam Whitford Sales Director: Jenna Clarke Office Manager: Rosa Pike</p>
      <h2>OUR TRADES PEOPLE</h2>
      <p>The core of our company: We have over 30 painters and trades ready to help with all your painting and remedial needs.<br>Through extensive training and employment procedures, we only employ and retain the best.</p>
    </aside>

    <span class="page-number" style="left:30px">4</span>
    <span class="web">www.brightwellworks.com.au</span>
  </section>

  <section class="page page--right">
    <header class="page-header">
      <span class="year-tag">2019</span>
      <span class="doc-title">CAPABILITY STATEMENT</span>
      <div class="brand">
        <div class="brand-name">Brightwell Works</div>
        <div class="brand-tagline">strata painting &amp; remedial repair</div>
      </div>
    </header>

    <div class="facts">
      <div class="facts-list">
        <h3>CREDENTIALS</h3>
        <p>A.B.N.: 48 302 771 586<br>A.C.N.: 302 771 586</p>
        <h3>LICENCES</h3>
        <p>Trade Contractor's Licence 'Builder' – 418922B<br>Supervisor Certificate 'Painter, Decorator' – 70254P</p>
        <h3>INSURANCES</h3>
        <p>Public Liability:<br>Harbourline Insurance, Combined General Liability - Policy Number<br>55 8830412 HL<br>Limit – $20,000,000</p>
        <h3>WORKCOVER:</h3>
        <p>Coastsure Workers Insurance - Policy Number 204418733</p>
      </div>
      <div class="quality">
        <h3>QUALITY ASSURANCE AND ETHICAL PRACTICE</h3>
        <p>Brightwell Works acts with integrity and in accordance with principles of good practice, ensuring quality always meets or exceeds legislative and industry standards.</p>
        <p>The Brightwell Works management hands-on approach assures the success of the company's quality system and total commitment to complete implementation in accordance with Australian Standard AS/NZS ISO9001:2008 Quality Management systems.</p>
        <p>We adhere to the Painters' Guild and Tilers' Guild Code of Ethics and to all codes of practice relative to our trades.</p>
      </div>
    </div>

    <div class="photo-desk" role="img" aria-label="Photo of a team working at a desk with notebooks, a laptop and a coffee cup"></div>

    <span class="page-number" style="left:30px">5</span>
    <span class="web">www.brightwellworks.com.au</span>
  </section>

</main>
</body>
</html>
```